KLT Business cards

I currently have a logo that was designed by a mark hive designer. I would like this to be added to the business card.

We are an innovative new start-up business offering finance solutions to the car dealership market in the UK. So our clients are quiet traditional, so are cards need to fit in, but at the same time show we are a modern online business.

Finance

```html
<!DOCTYPE html>
<html lang="en">
<head>
<meta charset="utf-8">
<title>KLT Business Cards</title>
<link rel="stylesheet" href="https://fonts.googleapis.com/css2?family=Exo+2:wght@400;500;600&display=swap">
<style>
  :root {
    --navy: #0f1d45;
    --silver: #c9cdd2;
    --ink: #1a1f2e;
    --paper: #ffffff;
    --backdrop: #e4e5e7;
    --marker: #d6d9de;
  }
  * { margin: 0; padding: 0; box-sizing: border-box; }
  html, body { width: 1200px; height: 1021px; overflow: hidden; }
  body {
    background: var(--backdrop);
    font-family: "Exo 2", sans-serif;
    color: var(--ink);
    position: relative;
  }
  .card {
    position: absolute;
    left: 250px;
    width: 700px;
    height: 400px;
    background: var(--paper);
    overflow: hidden;
    box-shadow: 0 6px 18px rgba(0,0,0,0.12);
  }
  .card--front { top: 90px; }
  .card--back { top: 550px; }

  .brand {
    position: absolute;
    display: flex;
    align-items: center;
    gap: 12px;
  }
  .brand__dot {
    flex: none;
    border-radius: 50%;
    background: var(--marker);
  }
  .brand__name {
    font-weight: 500;
    color: var(--navy);
    line-height: 1.02;
  }
  .card--front .brand { left: 45px; top: 70px; }
  .card--front .brand__dot { width: 70px; height: 70px; }
  .card--front .brand__name { font-size: 27px; }
  .card--back .brand { left: 50%; top: 50%; transform: translate(-50%, -50%); gap: 16px; }
  .card--back .brand__dot { width: 106px; height: 106px; }
  .card--back .brand__name { font-size: 40px; }

  .person { position: absolute; left: 80px; top: 195px; }
  .person__name { font-size: 17px; font-weight: 600; color: var(--navy); letter-spacing: 0.5px; }
  .person__role { font-size: 13px; letter-spacing: 0.8px; margin-top: 2px; }

  .contact {
    position: absolute;
    right: 40px;
    top: 48px;
    text-align: right;
    font-size: 13px;
    letter-spacing: 0.8px;
    line-height: 1.25;
  }
  .contact__address { margin-bottom: 14px; }
  .contact__row { display: flex; justify-content: flex-end; align-items: center; gap: 6px; margin-bottom: 6px; }
  .contact__row svg { width: 13px; height: 13px; fill: var(--navy); }

  .swoosh { position: absolute; left: 0; bottom: 0; width: 700px; height: 400px; }
  .website {
    position: absolute;
    left: 40px;
    bottom: 22px;
    color: var(--paper);
    font-size: 14px;
    letter-spacing: 1px;
  }
</style>
</head>
<body>
  <section class="card card--front">
    <svg class="swoosh" viewBox="0 0 700 400" aria-hidden="true">
      <path d="M0,314 Q390,296 700,196 L700,212 Q390,312 0,330 Z" fill="var(--silver)"/>
      <path d="M0,330 Q390,312 700,212 L700,400 L0,400 Z" fill="var(--navy)"/>
    </svg>

    <div class="brand">
      <span class="brand__dot"></span>
      <span class="brand__name">Key Lane<br>Trading</span>
    </div>

    <div class="person">
      <p class="person__name">MARCUS HALE</p>
      <p class="person__role">OWNER/CEO</p>
    </div>

    <div class="contact">
      <p class="contact__address">Street, Region, Country<br>PO BOX 321</p>
      <p class="contact__row">012 345 6789
        <svg viewBox="0 0 16 16"><path d="M3 1l3 3-2 2c1 2 3 4 5 5l2-2 3 3-2 3C6 15 1 10 1 3z"/></svg></p>
      <p class="contact__row">012 345 6789
        <svg viewBox="0 0 16 16"><path d="M4 0h8v16H4z M5.5 2v10h5V2z"/></svg></p>
      <p class="contact__row">012 345 6789
        <svg viewBox="0 0 16 16"><path d="M4 0h7v5H4z M1 6h14v9H1z M3 9h4v2H3z"/></svg></p>
      <p class="contact__row">hello@keylanetrading.com
        <svg viewBox="0 0 16 16"><path d="M0 3h16v10H0z"/><path d="M0 3l8 6 8-6" fill="none" stroke="#fff" stroke-width="1.4"/></svg></p>
    </div>

    <p class="website">www.keylanetrading.com</p>
  </section>

  <section class="card card--back">
    <div class="brand">
      <span class="brand__dot"></span>
      <span class="brand__name">Key Lane<br>Trading</span>
    </div>
  </section>
</body>
</html>
```